The Steadfast Compass Method

I need an info graphic that shows how 7 habits help women in senior leadership to Mend Her Past, Steady Mind, and Sharpen Focus - leading to an increased Reach to Lead

https://clipvarn.tv/Qm7RxPz2KaL

7 habits are;

Bold Honesty
Restoring Inner Voice
Rooting In Faith
Regaining Balance
Rethinking
Staying Current
Giving Regard

My Colours are GOLD - BFA55E
White & Black

Fonts Playfair Display & Raleway

The style and feel should be 'high end' luxury quality corporate

Style - luxury

Target Market(s)

Women in senior leadership

Industry/Entity Type

Leadership

Font styles to use
Serif
Sans Serif

Colors
fece3e
fee18a

Requirements
Must have
• style
elegance
contemporary feel
use gold, #BFA55E - black and white creatively

Nice to have
• unusual

```html
<!DOCTYPE html>
<html lang="en">
<head>
<meta charset="utf-8">
<title>The Steadfast Compass Method – Reach to Lead</title>
<link rel="stylesheet" href="https://fonts.googleapis.com/css2?family=Playfair+Display:wght@400;600&display=swap">
<style>
  :root{
    --gold:#BFA55E;
    --gold-light:#fee18a;
    --gold-deep:#fece3e;
    --ink:#0b0b0b;
    --paper:#ffffff;
  }
  html,body{margin:0;padding:0;width:1200px;height:399px;overflow:hidden;background:var(--paper);}
  .framework-board{display:block;width:1200px;height:399px;}
  .label{font-family:"Playfair Display",Georgia,serif;text-anchor:middle;font-weight:400;}
  .habit-label{font-size:15px;fill:var(--habit-text);}
  .venn-label{font-size:17px;fill:var(--venn-text);}
  .core-word{font-size:21px;font-weight:600;letter-spacing:1.5px;fill:var(--core-text);}
  .habit-disc{fill:var(--disc-fill);stroke:url(#gold-edge);stroke-width:2.2;filter:url(#soft-shadow);}
  .habit-link{stroke:var(--gold);stroke-width:1.6;stroke-dasharray:2 5;stroke-linecap:round;fill:none;}
  .flow-arrow{fill:url(#gold-edge);}
  .gold-line{fill:none;stroke:url(#gold-edge);stroke-width:1.8;}
  .core-lens{fill:var(--lens-fill);}
  .variant--ink-on-paper{--disc-fill:url(#ink-disc);--habit-text:var(--paper);--venn-text:var(--paper);--core-text:var(--ink);--lens-fill:url(#gold-edge);}
  .variant--ink-on-night{--disc-fill:url(#ink-disc);--habit-text:var(--paper);--venn-text:var(--paper);--core-text:var(--ink);--lens-fill:url(#gold-edge);}
  .variant--paper-on-paper{--disc-fill:var(--paper);--habit-text:var(--ink);--venn-text:var(--ink);--core-text:var(--ink);--lens-fill:#f6ecd0;}
</style>
</head>
<body>
<svg class="framework-board" viewBox="0 0 2560 855" xmlns="http://www.w3.org/2000/svg" role="img" aria-label="Seven habits leading to the reach to lead, shown in three colour variants">
  <defs>
    <linearGradient id="gold-edge" x1="0" y1="0" x2="1" y2="1">
      <stop offset="0" stop-color="#fee18a"/>
      <stop offset="0.5" stop-color="#BFA55E"/>
      <stop offset="1" stop-color="#fece3e"/>
    </linearGradient>
    <linearGradient id="ink-disc" x1="0" y1="0" x2="1" y2="1">
      <stop offset="0" stop-color="#3a3b3f"/>
      <stop offset="1" stop-color="#050505"/>
    </linearGradient>
    <linearGradient id="night-panel" x1="0" y1="0" x2="1" y2="1">
      <stop offset="0" stop-color="#2f3035"/>
      <stop offset="1" stop-color="#000000"/>
    </linearGradient>
    <filter id="soft-shadow" x="-30%" y="-30%" width="160%" height="160%">
      <feDropShadow dx="3" dy="5" stdDeviation="5" flood-color="#000" flood-opacity="0.35"/>
    </filter>
    <clipPath id="clip-past"><circle cx="370" cy="300" r="120"/></clipPath>
    <clipPath id="clip-mind"><circle cx="488" cy="298" r="120"/></clipPath>

    <g id="core-lens">
      <g clip-path="url(#clip-past)"><g clip-path="url(#clip-mind)"><circle class="core-lens" cx="430" cy="400" r="120"/></g></g>
    </g>

    <g id="habit-ring">
      <path class="habit-link" d="M103 333 L137 480 L255 611 L430 661 L599 613 L722 480 L755 333"/>
      <circle class="habit-disc" cx="103" cy="333" r="59"/>
      <circle class="habit-disc" cx="137" cy="480" r="59"/>
      <circle class="habit-disc" cx="255" cy="611" r="59"/>
      <circle class="habit-disc" cx="430" cy="661" r="59"/>
      <circle class="habit-disc" cx="599" cy="613" r="59"/>
      <circle class="habit-disc" cx="722" cy="480" r="59"/>
      <circle class="habit-disc" cx="755" cy="333" r="59"/>
      <text class="label habit-label" x="103" y="330">Bold</text>
      <text class="label habit-label" x="103" y="347">Honesty</text>
      <text class="label habit-label" x="137" y="477">Restoring</text>
      <text class="label habit-label" x="137" y="494">Inner Voice</text>
      <text class="label habit-label" x="255" y="608">Rooting</text>
      <text class="label habit-label" x="255" y="625">In Faith</text>
      <text class="label habit-label" x="430" y="658">Regaining</text>
      <text class="label habit-label" x="430" y="675">Balance</text>
      <text class="label habit-label" x="599" y="618">Rethinking</text>
      <text class="label habit-label" x="722" y="477">Staying</text>
      <text class="label habit-label" x="722" y="494">Current</text>
      <text class="label habit-label" x="755" y="330">Giving</text>
      <text class="label habit-label" x="755" y="347">Regard</text>
      <path class="flow-arrow" d="M186 326 L199 333 L186 340 Z"/>
      <path class="flow-arrow" d="M208 436 L222 436 L215 449 Z"/>
      <path class="flow-arrow" d="M306 528 L306 542 L293 535 Z"/>
      <path class="flow-arrow" d="M423 576 L437 576 L430 563 Z"/>
      <path class="flow-arrow" d="M548 530 L561 537 L548 544 Z"/>
      <path class="flow-arrow" d="M633 436 L647 436 L640 449 Z"/>
      <path class="flow-arrow" d="M671 326 L658 333 L671 340 Z"/>
    </g>

    <g id="venn-outlines">
      <circle class="gold-line" cx="370" cy="300" r="120"/>
      <circle class="gold-line" cx="488" cy="298" r="120"/>
      <circle class="gold-line" cx="430" cy="400" r="120"/>
    </g>

    <g id="venn-labels">
      <text class="label venn-label" x="316" y="282">Mend Her Past</text>
      <text class="label venn-label" x="544" y="276">Steady Mind</text>
      <text class="label venn-label" x="432" y="470">Sharpen Focus</text>
      <text class="label core-word" x="430" y="328">REACH TO</text>
      <text class="label core-word" x="430" y="353">LEAD</text>
    </g>
  </defs>

  <!-- Variant one: ink disc on paper, gold core -->
  <g class="variant variant--ink-on-paper">
    <circle cx="430" cy="332" r="200" fill="url(#ink-disc)" stroke="url(#gold-edge)" stroke-width="1.6" filter="url(#soft-shadow)"/>
    <use href="#core-lens"/>
    <use href="#venn-outlines"/>
    <use href="#venn-labels"/>
    <use href="#habit-ring"/>
  </g>

  <!-- Variant two: ink on night -->
  <rect x="856" y="0" width="860" height="855" fill="url(#night-panel)"/>
  <g class="variant variant--ink-on-night" transform="translate(856 0)">
    <circle class="gold-line" cx="430" cy="332" r="200"/>
    <use href="#core-lens"/>
    <use href="#venn-outlines"/>
    <use href="#venn-labels"/>
    <use href="#habit-ring"/>
  </g>

  <!-- Variant three: paper on paper -->
  <g class="variant variant--paper-on-paper" transform="translate(1716 0)">
    <circle cx="430" cy="332" r="200" fill="var(--paper)" stroke="url(#gold-edge)" stroke-width="1.6" filter="url(#soft-shadow)"/>
    <use href="#core-lens"/>
    <use href="#venn-outlines"/>
    <use href="#venn-labels"/>
    <use href="#habit-ring"/>
  </g>
</svg>
</body>
</html>
```